Flyer for the Harvest Lantern Gathering 2018

Design a flyer for our annual conference with basic information about the conference: conference logo and year,

Location:
Tolvane Community Center (Downtown Portland)
482 Wexmoor Street, Portland, ME 04107,

Date:
August 24th, 25th and 26th, 2018
Start time 6:00PM

I would like the following three words added to the flyer. These words describe the vision of the conference:
Prophetic, Worship, Prayer

```html
<!DOCTYPE html>
<html lang="en">
<head>
<meta charset="utf-8">
<title>Harvest Lantern Gathering 2018 — Flyer</title>
<link rel="stylesheet" href="https://fonts.googleapis.com/css2?family=Exo+2:wght@500;600;700&family=Michroma&family=Courgette&display=swap">
<style>
  :root {
    --page-bg: #d6d6d6;
    --ink-white: #ffffff;
    --ink-dark: #2a1a10;
    --brown-deep: #1e0f06;
    --brown-mid: #4a2a0e;
    --glow-gold: #f7c531;
    --amber: #e0a21f;
    --olive-gold: #c7a51f;
    --orange: #d9681b;
    --orange-deep: #b8481a;
    --ring-orange: #f0901e;
  }
  * { margin: 0; padding: 0; box-sizing: border-box; }
  html, body {
    width: 1200px; height: 2250px; overflow: hidden;
    background: var(--page-bg);
  }
  .flyer {
    position: absolute; left: 50px; top: 345px;
    width: 1100px; height: 1560px; overflow: hidden;
    background: var(--orange);
    box-shadow: 0 20px 40px rgba(0,0,0,0.35);
    color: var(--ink-white);
    text-align: center;
  }
  .hero-art {
    position: absolute; inset: 0 0 auto 0; height: 900px;
    background:
      radial-gradient(ellipse 380px 340px at 50% 34%, rgba(247,197,49,0.95), rgba(224,162,31,0.55) 45%, rgba(74,42,14,0) 80%),
      linear-gradient(180deg, var(--brown-mid) 0%, var(--brown-deep) 55%, #140904 100%);
  }
  .lower-field {
    position: absolute; inset: 0;
  }
  .title {
    position: absolute; left: 0; right: 0; top: 62px;
    font-family: "Exo 2", sans-serif; font-weight: 600;
    font-size: 74px; line-height: 82px; letter-spacing: 1px;
    text-transform: uppercase;
    text-shadow: 0 3px 8px rgba(0,0,0,0.5);
  }
  .emblem {
    position: absolute; left: 364px; top: 537px;
    width: 374px; height: 374px; border-radius: 50%;
    background: var(--ink-white);
    border: 6px solid var(--ring-orange);
    display: flex; align-items: center; justify-content: center;
  }
  .emblem-name {
    font-family: "Exo 2", sans-serif; font-weight: 600;
    font-size: 62px; letter-spacing: 3px; color: var(--ink-dark);
  }
  .vision {
    position: absolute; left: 0; right: 0; top: 950px;
    font-family: "Michroma", sans-serif; font-size: 38px;
    letter-spacing: 2px; text-transform: uppercase;
    display: flex; justify-content: center; align-items: center; gap: 34px;
    text-shadow: 0 2px 4px rgba(0,0,0,0.35);
  }
  .vision-dot {
    width: 22px; height: 22px; border-radius: 50%; background: var(--ink-white);
  }
  .info-label {
    position: absolute; left: 0; right: 0;
    font-family: "Courgette", cursive; font-size: 52px; line-height: 60px;
  }
  .info-text {
    position: absolute; left: 0; right: 0;
    font-family: "Exo 2", sans-serif; font-weight: 500;
    font-size: 35px; line-height: 42px;
  }
  .venue-label { top: 1058px; }
  .venue-text  { top: 1128px; }
  .date-label  { top: 1240px; }
  .date-text   { top: 1306px; }
  .time-label  { top: 1376px; }
  .time-text   { top: 1444px; }
</style>
</head>
<body>
  <main class="flyer">
    <svg class="lower-field" width="1100" height="1560" viewBox="0 0 1100 1560" aria-hidden="true">
      <defs>
        <linearGradient id="fieldGradient" x1="0" y1="0" x2="0.4" y2="1">
          <stop offset="0" stop-color="#c9a81f"/>
          <stop offset="0.35" stop-color="#dc9a1f"/>
          <stop offset="0.7" stop-color="#d9681b"/>
          <stop offset="1" stop-color="#b8481a"/>
        </linearGradient>
        <radialGradient id="fieldShade" cx="0.95" cy="0.55" r="0.6">
          <stop offset="0" stop-color="#7a2e0c" stop-opacity="0.45"/>
          <stop offset="1" stop-color="#7a2e0c" stop-opacity="0"/>
        </radialGradient>
      </defs>
      <rect width="1100" height="1560" fill="url(#fieldGradient)"/>
      <rect width="1100" height="1560" fill="url(#fieldShade)"/>
    </svg>

    <div class="hero-art" role="img" aria-label="Glowing cross above a crowd of worshippers with raised hands, in silhouette"
         style="clip-path: polygon(0 0, 100% 0, 100% 90.5%, 50% 82%, 0 90.5%);"></div>

    <svg style="position:absolute;left:0;top:0" width="1100" height="1560" viewBox="0 0 1100 1560" aria-hidden="true">
      <polygon class="divider-band" points="0,815 550,740 1100,815 1100,893 550,780 0,893" fill="#ffffff"/>
    </svg>

    <h1 class="title">Harvest Lantern<br>Gathering 2018</h1>

    <div class="emblem"><span class="emblem-name">HARLAN</span></div>

    <p class="vision">
      <span>Prophetic</span><span class="vision-dot"></span>
      <span>Worship</span><span class="vision-dot"></span>
      <span>Prayer</span>
    </p>

    <h2 class="info-label venue-label">Venue</h2>
    <p class="info-text venue-text">Tolvane Community Center (Downtown Portland)<br>482 Wexmoor Street, Portland, ME 04107,</p>

    <h2 class="info-label date-label">Date</h2>
    <p class="info-text date-text">August 24th, 25th and 26th, 2018</p>

    <h2 class="info-label time-label">Time</h2>
    <p class="info-text time-text">6:00PM&nbsp; onwards</p>
  </main>
</body>
</html>
```